IG ad to attract older men for better health #1

I want a bold headline Instagram Ad that coordinate with my website design with a racy sexy woman to attract men 45yrs old plus. See Two samples attached

Target Market(s)

Men 45 years old and older

Industry/Entity Type

Health And Wellness

Requirements
Must have
• eye catching appeal to men
Nice to have
• The copy to read
Kestrel61go is the headline at the top of the page. Then the copy reads...
"I want to seduce you to better health with a little T&A. Remove the excuses, provide ridiculously simple tips and advice to get you started on a path of lasting heath." Want more?

```html
<!DOCTYPE html>
<html lang="en">
<head>
<meta charset="utf-8">
<title>Kestrel61go — Instagram Ad</title>
<link href="https://fonts.googleapis.com/css2?family=Teko:wght@600&family=Roboto:wght@400;500&display=swap" rel="stylesheet">
<style>
  :root {
    --bg-dark: #121212;
    --bg-mid: #2c2c2c;
    --headline: #f7ea0e;
    --text: #ffffff;
    --banner: #9c0c10;
    --sheet-light: #eef0f3;
    --sheet-shadow: #b9bec6;
    --skin-light: #e9c3aa;
    --skin-dark: #7a5848;
  }
  html, body {
    margin: 0;
    padding: 0;
    width: 1200px;
    height: 1200px;
    overflow: hidden;
    background: var(--bg-dark);
  }
  .ad {
    position: relative;
    width: 1200px;
    height: 1200px;
    overflow: hidden;
    background: linear-gradient(110deg, var(--bg-mid) 0%, #1c1c1c 45%, var(--bg-dark) 100%);
    font-family: "Roboto", Arial, sans-serif;
  }
  .photo-bed {
    position: absolute;
    left: 0;
    top: 845px;
    width: 1200px;
    height: 355px;
    background: linear-gradient(180deg, var(--sheet-light) 0%, #dfe2e7 45%, var(--sheet-shadow) 100%);
  }
  .photo-model {
    position: absolute;
    left: 90px;
    top: 34px;
    width: 430px;
    height: 1080px;
    border-radius: 160px 160px 40px 40px;
    background: linear-gradient(180deg, #d9b48a 0%, var(--skin-light) 22%, #2a2226 40%, var(--skin-light) 55%, #241d20 68%, var(--skin-dark) 100%);
    opacity: 0.9;
  }
  .headline {
    position: absolute;
    right: 48px;
    top: 22px;
    margin: 0;
    font-family: "Teko", "Arial Narrow", sans-serif;
    font-weight: 600;
    font-size: 132px;
    line-height: 1;
    letter-spacing: 4px;
    color: var(--headline);
    text-transform: uppercase;
  }
  .pitch {
    position: absolute;
    right: 72px;
    top: 282px;
    margin: 0;
    width: 560px;
    text-align: right;
    font-size: 31px;
    line-height: 59px;
    letter-spacing: 0.5px;
    color: var(--text);
  }
  .cta {
    position: absolute;
    left: 578px;
    top: 656px;
    width: 622px;
    height: 212px;
  }
  .cta svg { position: absolute; inset: 0; }
  .cta-label {
    position: absolute;
    left: 136px;
    top: 52px;
    margin: 0;
    font-weight: 500;
    font-size: 70px;
    line-height: 1.2;
    color: var(--text);
  }
</style>
</head>
<body>
  <main class="ad">
    <div class="photo-bed" role="img" aria-label="White rumpled bed sheets across the bottom of the ad"></div>
    <div class="photo-model" role="img" aria-label="Photo of a blonde woman in black lace lingerie kneeling on the bed"></div>

    <h1 class="headline">Kestrel61go</h1>

    <p class="pitch">"I want to seduce you to better<br>health with a little T&amp;A.<br>Remove the excuses, provide<br>ridiculously simple tips and<br>advice to get you started on a<br>path of lasting heath."</p>

    <div class="cta">
      <svg width="622" height="212" viewBox="0 0 622 212" aria-hidden="true">
        <polygon points="0,0 622,20 622,188 0,212 88,106" fill="var(--banner)"/>
      </svg>
      <p class="cta-label">Want more?</p>
    </div>
  </main>
</body>
</html>
```